BrookVale Collision Repair Web Site

Create a web site that will inform my potential customers about the services I provide. We are a Automotive Collision repair business that uses the latest state of the art equipment, computerized paint matching highly trained technicians, have over 30 years experience. We work with all all insurance programs. Our Moto is "Fixed Right, The First Time, Every Time". BrookVale, The trusted pick in collision repair.

Target Market(s)

People that have been in a auto collision, needs windshield replaced, people that drive 10 year or newer cars

Industry/Entity Type

Automotive

Coding

Coded - Design and coding required

Number of Pages Required

4 page

Font styles to use
Sans Serif

Requirements
Must have
• Logo, Place for Phone number, I need to be able to put the code in so I can use a tracking phone number
• site needs to be mobile ready or adaptive
• May want to have a photo of a high end car
• here is a web site for example with the pages that I want
• https://www.pondlyautobody.example/online-repair-estimate,
• https://www.pondlyautobody.example/schedule-appointment
• https://www.pondlyautobody.example/collision-repair/auto-body-repair
• https://www.pondlyautobody.example/contact
Nice to have
• Be great if the Car in the log could have the front damaged then have it fix in a animation. Not sure if could be done here

```html
<!DOCTYPE html>
<html lang="en">
<head>
<meta charset="utf-8">
<title>BrookVale Collision Repair</title>
<link href="https://fonts.googleapis.com/css2?family=Montserrat:ital,wght@0,400;0,600;0,700;1,800&display=swap" rel="stylesheet">
<style>
:root{
  --blue:#0a4f9f;
  --blue-dark:#063d80;
  --nav-top:#1b6fd6;
  --nav-bottom:#0b56b4;
  --btn:#3a95ea;
  --green:#9acd32;
  --ink:#222;
  --muted:#333;
  --footer:#2b2b2b;
  --white:#fff;
}
*{margin:0;padding:0;box-sizing:border-box}
html,body{width:737px;height:1200px;overflow:hidden;background:var(--white)}
body{font-family:"Montserrat",sans-serif;color:var(--ink);position:relative}
.abs{position:absolute}

/* header */
.brand{left:138px;top:12px;width:132px;text-align:center;color:var(--blue);font-weight:700;line-height:1.05}
.brand .name{font-size:22px;display:block}
.brand .sub{font-size:11px;display:block;letter-spacing:.5px}
.contact-info{left:462px;top:13px;font-size:6.6px;line-height:9.6px;color:var(--muted)}
.social{top:14px;width:19px;height:19px;background:var(--blue);border-radius:2px}
.find-us{left:605px;top:14px;width:33px;height:32px;border:1px solid #999;border-radius:3px;background:#e8e8e8}

/* nav */
.nav{left:0;top:63px;width:737px;height:29px;background:linear-gradient(var(--nav-top),var(--nav-bottom));}
.nav a{position:absolute;top:10px;font-size:6.8px;font-weight:700;color:var(--white);text-decoration:none}
.nav a.active{color:var(--green)}

/* hero */
.hero{left:0;top:92px;width:737px;height:269px;background:radial-gradient(ellipse at 72% 45%,#d42a26 0%,#b51d1b 30%,#5a5656 60%,#cfcfcf 100%)}
.hero-title{left:24px;top:100px;width:248px;height:44px;background:var(--blue);color:var(--white);font-size:12.5px;font-weight:700;line-height:17px;padding:4px 5px;letter-spacing:-.3px;white-space:nowrap;overflow:hidden}
.point{left:24px;width:248px;background:rgba(255,255,255,.9);font-size:6.2px;line-height:9px;color:var(--muted);padding:4px 8px;border-bottom:1px solid #bbb}
.btn{display:block;background:var(--btn);color:var(--white);font-size:6.6px;font-weight:700;text-align:center;text-decoration:none}
.hero-tag{right:8px;top:287px;font-size:12px;font-weight:800;font-style:italic;color:var(--white);white-space:nowrap;letter-spacing:-.2px}
.hero-sub{left:436px;top:309px;font-size:7.4px;font-weight:700;color:var(--white);white-space:nowrap}

/* welcome */
.welcome-title{left:0;width:737px;top:367px;text-align:center;font-size:15.5px;font-weight:700}
.welcome-text{left:152px;top:390px;width:432px;text-align:center;font-size:6.2px;line-height:9.4px;color:var(--muted)}
.rule{left:150px;top:441px;width:438px;height:1px;background:#bbb}
.est-title{left:154px;top:459px;font-size:11.5px;font-weight:700}
.est-text{left:154px;top:480px;width:205px;font-size:6.2px;line-height:9.3px;color:var(--muted)}

/* safety */
.safety{left:0;top:605px;width:737px;height:238px;background:var(--blue)}
.safety-title{left:154px;top:617px;font-size:14.5px;font-weight:700;color:var(--white);line-height:17px}
.safety-text{font-size:6.2px;line-height:9.3px;color:var(--white);font-weight:600}
.safety-head{color:var(--green);font-weight:700}

/* faq */
.faq-band{left:0;top:843px;width:737px;height:285px;background:linear-gradient(90deg,#27468f 0%,#3a5ca5 20%,#c9a48a 30%,#e9eef3 45%,#f3f5f7 70%,#c9d2dc 100%)}
.faq-title{left:357px;top:852px;font-size:11px;font-weight:700}
.faq-q{left:374px;width:214px;background:var(--blue);color:var(--white);font-size:6.3px;line-height:9.3px;font-weight:600;text-align:center;display:flex;align-items:center;justify-content:center;padding:0 6px}

.reviews{left:0;width:737px;top:1141px;text-align:center;font-size:8px;font-weight:700}
.footer{left:0;top:1166px;width:737px;height:34px;background:var(--footer);color:var(--white);font-size:6.5px;font-weight:600;text-align:center;line-height:34px}
</style>
</head>
<body>

<header>
  <div class="abs brand"><span class="name">BrookVale</span><span class="sub">Collision Repair</span></div>
  <div class="abs contact-info">Call Us: 800-555-5555<br>1234 N. Street Address,<br>STATE. 00000</div>
  <div class="abs social" style="left:551px"></div>
  <div class="abs social" style="left:574px"></div>
  <div class="abs find-us">
    <svg width="33" height="32" viewBox="0 0 33 32"><path d="M16.5 5a5 5 0 0 0-5 5c0 4 5 9 5 9s5-5 5-9a5 5 0 0 0-5-5z" fill="#d62b25"/><circle cx="16.5" cy="10" r="1.8" fill="#fff"/><text x="16.5" y="28" font-size="5.5" font-family="Montserrat,sans-serif" font-weight="700" text-anchor="middle" fill="#222">FIND US</text></svg>
  </div>
</header>

<nav class="abs nav">
  <a class="active" href="#" style="left:262px">HOME</a>
  <a href="#" style="left:302px">ABOUT</a>
  <a href="#" style="left:344px">SERVICES ⌄</a>
  <a href="#" style="left:405px">FAQS</a>
  <a href="#" style="left:442px">CONTACT</a>
</nav>

<section>
  <div class="abs hero" role="img" aria-label="Close-up photo of a red high-end sports car headlight"></div>
  <h1 class="abs hero-title">Why is BrookVale the Intelligent<br>Choice in Collision Repair?</h1>
  <p class="abs point" style="top:147px;height:29px">We ensure that latest OEM approved procedures are followed during each phase of the repair of your vehicle.</p>
  <p class="abs point" style="top:178px;height:19px">We have the latest in computerized frame equipment.</p>
  <p class="abs point" style="top:200px;height:36px">Our technicians are certified in structural repairs ensuring that your vehicle will be as safe for your family as it was the day it left the factory.</p>
  <p class="abs point" style="top:239px;height:27px">Our refinish equipment and trained painters will make sure your finish is back to factory finish maybe even better.</p>
  <p class="abs point" style="top:270px;height:26px">Each repair including paint and collision repair comes with a limited lifetime warranty as long as you own the vehicle.</p>
  <a class="abs btn" href="#" style="left:89px;top:306px;width:117px;height:24px;line-height:24px">SCHEDULE AN APPOINTMENT</a>
  <p class="abs hero-tag">Fixed Right, The First Time, Every Time</p>
  <p class="abs hero-sub">BrookVale, The trusted pick in collision repair.</p>
</section>

<section>
  <h2 class="abs welcome-title">Welcome to our Collision Center</h2>
  <p class="abs welcome-text">For over 30 years' vehicle owners and fleet managers have trusted our staff for all their collision repairs. Our Nationwide, Lifetime Guarantee and excellent customer service are just a few of the reasons you want to choose BrookVale. We use the latest computerized frame alignment and paint matching technology. Our professional staff of certified technicians take pride in the work they do and strive to deliver the best possible service. BrookVale "The trusted pick in Collision Repair"</p>
  <div class="abs rule"></div>
  <h2 class="abs est-title">Need an estimate?</h2>
  <p class="abs est-text">Walk in estimates are welcome but we prefer to have you call us and schedule your appointment to have your estimate written. This will make sure you don't have to wait any longer than necessary and it will give us proper time to thoroughly inspect your vehicle.<br><br>Already have an estimate completed by your insurance company? Email us your insurance estimate.</p>
  <a class="abs btn" href="#" style="left:199px;top:572px;width:116px;height:22px;line-height:22px">ONLINE ESTIMATE</a>
</section>

<section>
  <div class="abs safety"></div>
  <h2 class="abs safety-title">Is your car safe<br>to drive?</h2>
  <p class="abs safety-text" style="left:154px;top:656px;width:132px">First, we hope that no one was injured in the unfortunate event that led you to search for a collision repair facility and we are glad you found us. Now we want to make sure we can help you mitigate any further loss or property or worse yet physical harm.Your car was just involved in a collision and depending on how severe the accident was it is possible that one or more of the many systems the manufacture of your vehicle has designed into your vehicle are no longer able to protect you if you get into another accident before proper repairs have been made.</p>
  <p class="abs safety-head" style="left:304px;top:613px;font-size:7.6px">Some examples of this maybe:</p>
  <p class="abs safety-text" style="left:313px;top:634px;width:113px">If any airbags have been deployed or your airbag light is on after an impact. Your vehicle is not safe to drive. Please call us or have your car towed straight to our shop. Your vehicle is not safe to drive.<br><br>If any seatbelts no longer retract after an accident. Your vehicle is not safe to drive.</p>
  <p class="abs safety-text safety-head" style="left:453px;top:613px;width:128px">Listed below are a few examples of impacts that may have compromised your vehicle's safety devices.</p>
  <p class="abs safety-text" style="left:462px;top:650px;width:110px">If you had a front or rear impact of a speed greater than 5 miles per hour.<br><br>If your doors don't open properly after a front or rear impact.<br><br>If your window will not roll down after a side impact, the intrusion beam may be compromised and the vehicle may not be safe to drive.<br><br>If you are not sure if your car is safe to drive, please give us a call immediately or get your vehicle in to have it inspected. There is no cost for a visual inspection.</p>
</section>

<section>
  <div class="abs faq-band" role="img" aria-label="Photo of a mechanic in blue overalls holding a wrench in a bright workshop"></div>
  <h2 class="abs faq-title">FAQ</h2>
  <p class="abs faq-q" style="top:874px;height:32px">Q: I have an insurance estimate already do I need to get more estimates?</p>
  <p class="abs faq-q" style="top:914px;height:22px">Q: Can you see all the damage during the estimate?</p>
  <p class="abs faq-q" style="top:944px;height:41px">Q: I got in an accident and the person that hit me wants to pay to repair my car without filing an insurance claim. Is this a good idea?</p>
  <p class="abs faq-q" style="top:994px;height:40px">Q: My final bill was greater than the estimate. Why can't you write an estimate that will include everything that my car will need for repairs?</p>
  <p class="abs faq-q" style="top:1042px;height:32px">Q: Why will you have to blend paint into the panels adjacent to the repairs that need to be done on my vehicle?</p>
  <p class="abs faq-q" style="top:1082px;height:31px">Q: Why doesn't the paint on my bumper match the paint on the rest of my vehicle?</p>
</section>

<h2 class="abs reviews">Reviews</h2>
<footer class="abs footer">Copyright 2016 | BrookVale Collision Repair - All rights reserved</footer>

</body>
</html>
```